Website Landing Page for Brightfall Systems

Create a custom designed website landing page for our business. Looking for a professional upscale design that incorporates our logo and logo colors into the theme. I want a standard fixed frame website, not a constant scrolling format that seems to be the trend. To start with I'm looking for more of the graphic design part, maybe a concept or theme, I don't expect to see a finished project. Not interested in generic templates or layouts.

The name of our company is Brightfall Systems and I've attached our logo below. I'd like to have the web page have the same look and feel of our logo, as well as the colors. Our company, Brightfall Systems does system design, installation, and programming, of residential and commercial Audio/Video and Automation systems. We do home theaters, lighting and building automation, video conferencing systems, security camera installations, conference rooms, projectors, distributed audio systems, and similar Technology projects. This will be a professional services/informational website. We will not sell products on this website. This website will be used to advertise our company and communicate our services to prospective customers. Having a well designed, professional and clean website is one way we want to distinguish our company from the competition.

Here are some examples of what I consider a professional well designed website
http://www.qorlamstudio.com/Work/

Last year we had our tradlo store designed (with PixelMarket) and I'm really happy with the way it turned out. You can see it at www.HolvenGearDepot.com I consider this to be a great design and looking for the same level of quality with this new website. However, do not copy or use any part of this design in this new project. This tradlo store is completely separate from our other company Brightfall Systems. I only mention this tradlo store an an example of good work.

Reason: Still going through designs.

Reason: Still working on project and have not had time to review all designs and request revisions.

Reason: Sill going through designs and requesting revisions

Reason: still going through all the submissions we received.

Target Market(s)

People interested in Audio/Video, home theaters, home automation. We do sales, system design, and programming. We typically work on larger projects with both residential and commercial customers.

Industry/Entity Type

Business

Number of Pages Required

1 page

Requirements
Must have
• Great design elements. Please use a white background. I think white goes well with our logo colors.

```html
<!DOCTYPE html>
<html lang="en">
<head>
<meta charset="utf-8">
<title>Brightfall Systems</title>
<link href="https://fonts.googleapis.com/css2?family=Roboto+Condensed:wght@400;700&family=Open+Sans:ital,wght@0,400;0,600;0,700;1,300;1,400&display=swap" rel="stylesheet">
<style>
:root{
  --green:#62b446;
  --ink:#3c3c3c;
  --muted:#9a9a9a;
  --line:#d9d9d9;
  --white:#ffffff;
  --caption:#2b2b2b;
  --panel:#f0f0f0;
}
*{box-sizing:border-box;margin:0;padding:0}
html,body{width:1200px;height:2270px;overflow:hidden;background:var(--white)}
body{position:relative;font-family:"Open Sans",Arial,sans-serif;color:var(--ink)}
.abs{position:absolute}

/* hero */
.hero{left:0;top:0;width:1200px;height:605px;background:linear-gradient(180deg,#e6eaef 0%,#dfe3e6 55%,#cfd3cc 100%)}
.hero-cut{left:0;top:0}
.brand{left:128px;top:44px;display:flex;align-items:center;gap:12px}
.brand-name{font-family:"Roboto Condensed",Arial,sans-serif;font-weight:400;font-size:26px;line-height:30px;color:#333}
.nav{left:540px;top:48px;display:flex;list-style:none}
.nav li{font-family:"Roboto Condensed",Arial,sans-serif;font-size:17px;color:#333;margin-right:45px}
.nav li:last-child{margin-right:0}
.nav .active{color:var(--green)}
.hero-title{left:0;width:1200px;top:238px;text-align:center;font-family:"Roboto Condensed",Arial,sans-serif;font-weight:700;font-size:36px;color:var(--green);text-transform:uppercase}
.hero-sub{left:310px;width:580px;top:300px;text-align:center;font-family:"Roboto Condensed",Arial,sans-serif;font-style:italic;font-size:17px;line-height:28px;color:#333}
.scroll-btn{left:583px;top:531px;width:34px;height:48px;border:2px solid #555;border-radius:17px}

/* sections */
.section-title{left:0;width:1200px;text-align:center;font-family:"Roboto Condensed",Arial,sans-serif;font-weight:700;font-size:34px;color:var(--green);text-transform:uppercase}
.section-lead{left:220px;width:760px;text-align:center;font-style:italic;font-weight:300;font-size:14px;line-height:23px;color:var(--muted)}

.service{width:230px;text-align:center}
.service-icon{width:133px;height:133px;margin:0 auto;border-radius:50%;border:1px solid var(--line);background:linear-gradient(135deg,#fff 0%,#fff 50%,#f1f1f1 50%,#f6f6f6 100%);display:flex;align-items:center;justify-content:center}
.service-name{margin-top:24px;font-family:"Roboto Condensed",Arial,sans-serif;font-weight:400;font-size:19px;color:#555;text-transform:uppercase}
.service-text{margin:9px auto 0;width:210px;font-style:italic;font-weight:300;font-size:12px;line-height:21px;color:var(--muted)}
.service-btn{display:block;margin:23px auto 0;width:121px;height:42px;border:1px solid #cfcfcf;border-radius:21px;line-height:40px;font-size:11px;font-weight:600;color:#555;text-transform:uppercase}

.dots{left:578px;top:1177px;display:flex;gap:7px}
.dot{width:10px;height:10px;border-radius:50%;background:#d4d4d4}
.dot.on{background:var(--green)}

.tile{top:1412px;width:229px;height:274px}
.tile-photo{width:229px;height:228px}
.tile-bar{height:46px;background:var(--caption);color:var(--white);font-family:"Roboto Condensed",Arial,sans-serif;font-size:15px;line-height:46px;padding-left:11px;text-transform:uppercase;position:relative}
.tile-bar svg{position:absolute;right:11px;top:16px}

/* footer */
.footer{left:0;top:1748px;width:1200px;height:522px;background:radial-gradient(ellipse at 40% 40%,#9b9c9e 0%,#8c8d8f 55%,#7e7f81 100%)}
.contact-card{left:127px;top:1828px;width:622px;height:375px;background:var(--white)}
.contact-info{left:146px;top:1873px;width:270px}
.contact-head{font-size:14px;font-weight:700;color:var(--green);text-transform:uppercase}
.contact-lead{margin-top:16px;font-size:12px;font-weight:700;line-height:20px;color:#666}
.contact-label{margin-top:20px;font-size:12px;font-weight:700;color:var(--green);text-transform:uppercase;display:flex;align-items:center;gap:6px}
.contact-value{margin-top:6px;font-size:11px;color:#222}
.map{left:439px;top:1828px;width:310px;height:375px;background:linear-gradient(160deg,#e6e6e4 0%,#dcdcda 60%,#d3d3d1 100%)}
.comment-card{left:772px;top:1828px;width:298px;height:375px;background:var(--panel)}
.comment-head{left:789px;top:1874px;font-family:"Roboto Condensed",Arial,sans-serif;font-weight:700;font-size:16px;color:#555;text-transform:uppercase}
.field{left:789px;width:264px;border:1px solid #a8a8a8;background:#f7f7f7;font-size:10px;color:#777;padding:8px 12px}
.submit{left:873px;top:2132px;width:97px;height:33px;border-radius:17px;background:var(--green);color:var(--white);font-size:12px;font-weight:700;text-align:center;line-height:33px;text-transform:uppercase}
.copyright{left:0;width:1200px;top:2233px;text-align:center;font-size:10px;color:#a3a3a5}
</style>
</head>
<body>

<!-- hero -->
<div class="abs hero" role="img" aria-label="Pale washed-out photograph of a city skyline with office towers under a cloudy sky"></div>
<svg class="abs hero-cut" width="1200" height="606" viewBox="0 0 1200 606">
  <polygon points="0,428 600,605 0,605" fill="#fff"/>
  <polygon points="1200,428 600,605 1200,605" fill="#fff"/>
</svg>

<div class="abs brand">
  <span class="brand-name">Brightfall Systems</span>
</div>

<ul class="abs nav">
  <li class="active">Home</li>
  <li>About us</li>
  <li>Download</li>
  <li>Pricing</li>
  <li>Blog</li>
  <li>Contact</li>
</ul>

<h1 class="abs hero-title">Cras tempor tortor venenatis vulputate</h1>
<p class="abs hero-sub">Suspendisse potenti. Vestibulum diam erat, finibus eget arcu sed, interdum venenatis ligula. Nulla posuere orci facilisis elit posuere elementum.</p>
<div class="abs scroll-btn">
  <svg width="30" height="44" viewBox="0 0 30 44"><polyline points="10,22 15,27 20,22" fill="none" stroke="#555" stroke-width="2"/></svg>
</div>

<!-- services -->
<h2 class="abs section-title" style="top:682px">Services we offer</h2>
<p class="abs section-lead" style="top:735px">Nunc bibendum euismod nulla, eu aliquam massa laoreet in. Lorem ipsum dolor sit amet, consectetur adipiscing elit. Maecenas tellus purus, sodales vitae scelerisque sodales, lobortis a nunc.</p>

<div class="abs service" style="left:119px;top:839px">
  <div class="service-icon">
    <svg width="48" height="58" viewBox="0 0 48 58" fill="none" stroke="#555" stroke-width="2.4">
      <rect x="8" y="4" width="32" height="32" rx="5"/><circle cx="24" cy="20" r="9"/><circle cx="24" cy="20" r="3.5"/>
      <path d="M18 36v6h12v-6M16 42h16v4c0 5-16 5-16 0z"/>
    </svg>
  </div>
  <h3 class="service-name">Security camera</h3>
  <p class="service-text">Integer sit amet lacus fringilla, fringilla dolor vitae, imperdiet elit. Vivamus vitaedolor luctus venenatis.</p>
  <span class="service-btn">Know more</span>
</div>

<div class="abs service" style="left:363px;top:839px">
  <div class="service-icon">
    <svg width="58" height="58" viewBox="0 0 58 58" fill="none" stroke="#555" stroke-width="2">
      <circle cx="29" cy="8" r="4"/><path d="M23 22v-5c0-3 12-3 12 0v5"/><rect x="20" y="22" width="18" height="8"/>
      <g><circle cx="10" cy="37" r="3"/><circle cx="22" cy="37" r="3"/><circle cx="36" cy="37" r="3"/><circle cx="48" cy="37" r="3"/>
      <rect x="6" y="42" width="8" height="5"/><rect x="18" y="42" width="8" height="5"/><rect x="32" y="42" width="8" height="5"/><rect x="44" y="42" width="8" height="5"/>
      <rect x="3" y="48" width="52" height="6"/></g>
    </svg>
  </div>
  <h3 class="service-name">Conference rooms</h3>
  <p class="service-text">Integer sit amet lacus fringilla, fringilla dolor vitae, imperdiet elit. Vivamus vitaedolor luctus venenatis.</p>
  <span class="service-btn">Know more</span>
</div>

<div class="abs service" style="left:607px;top:839px">
  <div class="service-icon">
    <svg width="50" height="44" viewBox="0 0 50 44" fill="none" stroke="#555" stroke-width="2.2">
      <rect x="3" y="3" width="44" height="32" rx="2"/><path d="M12 40h26"/>
      <path d="M12 10v18M19 10v18M26 10v18M33 10v18M40 10v18"/>
      <path d="M9 22h6M16 14h6M23 24h6M30 16h6M37 20h6"/>
    </svg>
  </div>
  <h3 class="service-name">Home theaters</h3>
  <p class="service-text">Integer sit amet lacus fringilla, fringilla dolor vitae, imperdiet elit. Vivamus vitaedolor luctus venenatis.</p>
  <span class="service-btn">Know more</span>
</div>

<div class="abs service" style="left:850px;top:839px">
  <div class="service-icon">
    <svg width="56" height="48" viewBox="0 0 56 48" fill="none" stroke="#555" stroke-width="2.2">
      <circle cx="16" cy="11" r="8"/><circle cx="34" cy="11" r="8"/><circle cx="16" cy="11" r="2.5"/><circle cx="34" cy="11" r="2.5"/>
      <rect x="8" y="21" width="32" height="18" rx="2"/><path d="M40 26l12-6v20l-12-6"/><path d="M18 39l-4 7M30 39l4 7"/>
    </svg>
  </div>
  <h3 class="service-name">Projectors</h3>
  <p class="service-text">Integer sit amet lacus fringilla, fringilla dolor vitae, imperdiet elit. Vivamus vitaedolor luctus venenatis.</p>
  <span class="service-btn">Know more</span>
</div>

<div class="abs dots"><span class="dot on"></span><span class="dot"></span><span class="dot"></span></div>

<!-- showcase -->
<h2 class="abs section-title" style="top:1256px;font-size:28px">Donec egetdui tortor fusce</h2>
<p class="abs section-lead" style="top:1307px">Nunc bibendum euismod nulla, eu aliquam massa laoreet in. Lorem ipsum dolor sit amet, consectetur adipiscing elit. Maecenas tellus purus, sodales vitae scelerisque sodales, lobortis a nunc.</p>

<div class="abs tile" style="left:129px">
  <div class="tile-photo" role="img" aria-label="Photograph of a glass office building against a blue sky" style="background:linear-gradient(160deg,#3d78c4 0%,#8fb4dc 45%,#c9d6e2 100%)"></div>
  <div class="tile-bar">Litora torquent<svg width="8" height="14" viewBox="0 0 8 14"><polyline points="1,1 7,7 1,13" fill="none" stroke="#fff" stroke-width="2"/></svg></div>
</div>
<div class="abs tile" style="left:367px">
  <div class="tile-photo" role="img" aria-label="Photograph of a large auditorium with rows of seats and a lit ceiling" style="background:linear-gradient(180deg,#b9b3a7 0%,#8c8880 50%,#3a3b3e 100%)"></div>
  <div class="tile-bar">Litora torquent<svg width="8" height="14" viewBox="0 0 8 14"><polyline points="1,1 7,7 1,13" fill="none" stroke="#fff" stroke-width="2"/></svg></div>
</div>
<div class="abs tile" style="left:605px">
  <div class="tile-photo" role="img" aria-label="Photograph of a living room home theater with a large wall screen" style="background:linear-gradient(180deg,#3a3128 0%,#7c6a52 45%,#c9b79a 100%)"></div>
  <div class="tile-bar">Litora torquent<svg width="8" height="14" viewBox="0 0 8 14"><polyline points="1,1 7,7 1,13" fill="none" stroke="#fff" stroke-width="2"/></svg></div>
</div>
<div class="abs tile" style="left:844px">
  <div class="tile-photo" role="img" aria-label="Photograph of a modern bar interior with stools and hanging lights" style="background:linear-gradient(180deg,#2b2e33 0%,#4a4d52 45%,#8a6a48 100%)"></div>
  <div class="tile-bar">Litora torquent<svg width="8" height="14" viewBox="0 0 8 14"><polyline points="1,1 7,7 1,13" fill="none" stroke="#fff" stroke-width="2"/></svg></div>
</div>

<!-- footer -->
<div class="abs footer" role="img" aria-label="Faint grey world map backdrop"></div>

<div class="abs contact-card"></div>
<div class="abs contact-info">
  <h3 class="contact-head">Contact us</h3>
  <p class="contact-lead">Donec interdum dapibus facilisis aliquam congue tempus augue non bibendum ipsum dictum</p>
  <p class="contact-label"><svg width="9" height="12" viewBox="0 0 9 12"><path d="M4.5 0C2 0 0 2 0 4.5 0 8 4.5 12 4.5 12S9 8 9 4.5C9 2 7 0 4.5 0z" fill="#62b446"/><circle cx="4.5" cy="4.5" r="1.6" fill="#fff"/></svg>Location</p>
  <p class="contact-value">48 Orrin Street, Lakemoor</p>
  <p class="contact-label"><svg width="11" height="11" viewBox="0 0 11 11"><path d="M2 0l2 3-1.3 1.3c.8 1.6 2 2.8 3.5 3.5L7.5 6.5l3 2L9.5 11C4.5 11 0 6.5 0 1.5z" fill="#62b446"/></svg>Phone</p>
  <p class="contact-value">(+045) 222-555-0147</p>
  <p class="contact-label"><svg width="12" height="9" viewBox="0 0 12 9"><rect width="12" height="9" fill="#62b446"/><polyline points="0,0 6,5 12,0" fill="none" stroke="#fff" stroke-width="1.2"/></svg>Email</p>
  <p class="contact-value">hello@brightfallsys.com</p>
</div>
<div class="abs map" role="img" aria-label="Street map showing the office location on Marrow Lane with a red pin"></div>

<div class="abs comment-card"></div>
<h3 class="abs comment-head">Leave a comment</h3>
<div class="abs field" style="top:1918px;height:37px">Your Name</div>
<div class="abs field" style="top:1974px;height:37px">Your Email</div>
<div class="abs field" style="top:2030px;height:84px">Message</div>
<div class="abs submit">Submet</div>

<p class="abs copyright">Copyright © Brightfall Systems 2017. All rights reserved.</p>

</body>
</html>
```